Biz cards and stationary design
for Harbor Pathways
Project: Biz cards and stationary design
Biz cards and stationary design  - Consulting
Creative Brief
Professional
Tessa R Windrow
President
27816 Dovelin Court Haymarket, VA 20174
tessa.windrow@harborpathways-example.com
http://www.harborpathways-example.com

```html
<!DOCTYPE html>
<html lang="en">
<head>
<meta charset="utf-8">
<title>Harbor Pathways – Stationery Set</title>
<link href="https://fonts.googleapis.com/css2?family=Open+Sans:wght@400;600;700&display=swap" rel="stylesheet">
<style>
:root{
  --board:#ebe6de;
  --paper:#ffffff;
  --red:#b3121c;
  --red-dark:#7f0b12;
  --gold:#f0a526;
  --ink:#3a3a3a;
  --muted:#8a8a8a;
  --line:#b9b9b9;
  --faint:#f6e9e2;
}
*{margin:0;padding:0;box-sizing:border-box}
html,body{width:1200px;height:679px;overflow:hidden}
body{background:var(--board);font-family:"Open Sans",Arial,sans-serif;color:var(--ink);position:relative}
.item{position:absolute;background:var(--paper);box-shadow:0 2px 6px rgba(0,0,0,.18);overflow:hidden}
.item svg.wave{position:absolute;left:0;top:0;width:100%;height:100%}
.label{position:absolute;font-size:8px;font-weight:600;color:#4a4030;text-align:center;white-space:nowrap;z-index:3}
.brand{display:flex;align-items:center;gap:5px;font-weight:700;color:var(--red);letter-spacing:.5px;white-space:nowrap;position:relative;z-index:2}
.brand .dot{width:10px;height:10px;border-radius:50%;background:var(--gold)}
.brand.on-red{color:#fff}
.emblem-faint{position:absolute;border-radius:50%;background:radial-gradient(circle,var(--faint) 0%,rgba(246,233,226,.6) 60%,rgba(246,233,226,0) 72%)}

/* sheets */
.sheet{top:154px;width:352px;height:496px}
.fax{left:29px}
.letterhead{left:403px}
.sheet .brand{position:absolute;top:30px;left:0;right:0;justify-content:center;font-size:17px}
.sheet .emblem-faint{left:30px;top:140px;width:290px;height:290px}
.sheet .contact{position:absolute;right:16px;bottom:8px;font-size:5.5px;line-height:1.5;color:#fff;text-align:left;z-index:2;white-space:nowrap}

/* fax form */
.fax-title{position:absolute;top:62px;right:24px;font-size:9px;font-weight:700;color:var(--ink);z-index:2}
.fax-table{position:absolute;top:74px;left:20px;width:306px;border-collapse:collapse;font-size:6.5px;z-index:2}
.fax-table td{border:1px solid var(--line);height:16px;padding:0 4px;color:var(--ink)}
.fax-table td.key{width:46px}
.fax-checks{position:absolute;top:158px;left:20px;right:20px;display:flex;justify-content:space-between;font-size:6px;z-index:2;white-space:nowrap}
.fax-checks span::before{content:"";display:inline-block;width:6px;height:6px;border:1px solid var(--muted);margin-right:3px;vertical-align:-1px}

/* cards */
.card{top:43px;width:151px;height:77px}
.card.red{background:linear-gradient(135deg,var(--red) 0%,var(--red-dark) 100%)}
.card-1{left:504px}.card-2{left:672px}.card-3{left:838px}.card-4{left:1003px}
.card .brand{font-size:9px;gap:3px}
.card .brand .dot{width:6px;height:6px}
.card-1 .brand{position:absolute;top:8px;left:12px}
.card-1 .person{position:absolute;top:18px;left:58px;font-size:4px;line-height:1.35;color:var(--ink);z-index:2;white-space:nowrap}
.card-1 .person b{font-size:5px;color:var(--red)}
.card-2 .brand{position:absolute;top:12px;left:12px}
.card-3 .brand,.card-4 .brand{position:absolute;top:32px;left:0;right:0;justify-content:center}
.card-4 .emblem-faint{right:-20px;top:-15px;width:105px;height:105px;background:radial-gradient(circle,rgba(255,255,255,.12) 0%,rgba(255,255,255,0) 70%)}

/* envelopes */
.envelope-front{left:770px;top:158px;width:392px;height:185px}
.envelope-front .brand{position:absolute;top:14px;left:18px;font-size:13px}
.envelope-front .return{position:absolute;top:36px;left:24px;font-size:5.5px;color:var(--ink);z-index:2;white-space:nowrap}
.envelope-back-1{left:773px;top:360px;width:369px;height:200px}
.envelope-back-2{left:792px;top:461px;width:367px;height:187px}
.envelope-back-2 .brand{position:absolute;top:62px;left:0;right:0;justify-content:center;font-size:12px}
.envelope-back svg{position:absolute;left:0;top:0;width:100%;height:100%}
</style>
</head>
<body>

<!-- Fax cover -->
<div class="label" style="left:29px;width:352px;top:140px">Fax Cover</div>
<section class="item sheet fax">
  <div class="emblem-faint" role="img" aria-label="Faint brand emblem watermark"></div>
  <div class="brand"><span class="dot"></span>HARBOR PATHWAYS</div>
  <div class="fax-title">FAX</div>
  <table class="fax-table">
    <tr><td class="key">To:</td><td></td><td class="key">From:</td><td></td></tr>
    <tr><td class="key">Fax:</td><td></td><td class="key">Pages:</td><td></td></tr>
    <tr><td class="key">Phone:</td><td></td><td class="key">Date:</td><td></td></tr>
    <tr><td class="key">Re:</td><td></td><td class="key">CC:</td><td></td></tr>
  </table>
  <div class="fax-checks">
    <span>Urgent</span><span>For Review</span><span>Please Comment</span><span>Please Reply</span><span>Please Recycle</span>
  </div>
  <svg class="wave" viewBox="0 0 352 496" preserveAspectRatio="none">
    <path d="M0 462 C120 444 240 436 352 408 L352 420 C240 448 120 456 0 474Z" fill="var(--gold)"/>
    <path d="M0 476 C120 458 240 450 352 422 L352 496 L0 496Z" fill="var(--red)"/>
  </svg>
  <div class="contact">27816 Dovelin Court Haymarket, VA 20174<br>tessa.windrow@harborpathways-example.com<br>http://www.harborpathways-example.com</div>
</section>

<!-- Letterhead -->
<div class="label" style="left:403px;width:352px;top:140px">Letterhead</div>
<section class="item sheet letterhead">
  <div class="emblem-faint" role="img" aria-label="Faint brand emblem watermark"></div>
  <div class="brand"><span class="dot"></span>HARBOR PATHWAYS</div>
  <svg class="wave" viewBox="0 0 352 496" preserveAspectRatio="none">
    <path d="M0 462 C120 444 240 436 352 408 L352 420 C240 448 120 456 0 474Z" fill="var(--gold)"/>
    <path d="M0 476 C120 458 240 450 352 422 L352 496 L0 496Z" fill="var(--red)"/>
  </svg>
  <div class="contact">27816 Dovelin Court Haymarket, VA 20174<br>tessa.windrow@harborpathways-example.com<br>http://www.harborpathways-example.com</div>
</section>

<!-- Business cards -->
<section class="item card card-1">
  <svg class="wave" viewBox="0 0 151 77" preserveAspectRatio="none">
    <path d="M0 66 C50 63 100 60 151 54 L151 57 C100 63 50 66 0 69Z" fill="var(--gold)"/>
    <path d="M0 70 C50 67 100 64 151 58 L151 77 L0 77Z" fill="var(--red)"/>
  </svg>
  <div class="brand"><span class="dot"></span>HARBOR PATHWAYS</div>
  <div class="person"><b>Tessa R Windrow</b><br>President<br>27816 Dovelin Court Haymarket, VA 20174<br>tessa.windrow@harborpathways-example.com<br>http://www.harborpathways-example.com</div>
</section>
<section class="item card card-2 red">
  <svg class="wave" viewBox="0 0 151 77" preserveAspectRatio="none">
    <path d="M0 42 C50 26 100 19 151 22 L151 77 L0 77Z" fill="#fff"/>
    <path d="M0 38 C50 23 100 16 151 18 L151 22 C100 19 50 26 0 42Z" fill="var(--gold)"/>
  </svg>
  <div class="brand on-red"><span class="dot"></span>HARBOR PATHWAYS</div>
</section>
<section class="item card card-3">
  <svg class="wave" viewBox="0 0 151 77" preserveAspectRatio="none">
    <path d="M0 66 C50 63 100 61 151 53 L151 57 C100 65 50 67 0 70Z" fill="var(--gold)"/>
    <path d="M0 71 C50 68 100 66 151 58 L151 77 L0 77Z" fill="var(--red)"/>
  </svg>
  <div class="brand"><span class="dot"></span>HARBOR PATHWAYS</div>
</section>
<section class="item card card-4 red">
  <div class="emblem-faint" role="img" aria-label="Faint brand emblem decoration"></div>
  <div class="brand on-red"><span class="dot"></span>HARBOR PATHWAYS</div>
</section>

<!-- Envelope front -->
<div class="label" style="left:770px;width:392px;top:148px">Envelope (Front)</div>
<section class="item envelope-front">
  <div class="brand"><span class="dot"></span>HARBOR PATHWAYS</div>
  <div class="return">27816 Dovelin Court Haymarket, VA 20174</div>
  <svg class="wave" viewBox="0 0 392 185" preserveAspectRatio="none">
    <path d="M0 124 C130 148 260 126 392 92 L392 104 C260 138 130 158 0 136Z" fill="var(--gold)"/>
    <path d="M0 138 C130 160 260 140 392 106 L392 185 L0 185Z" fill="var(--red)"/>
  </svg>
</section>

<!-- Envelope back options -->
<div class="label" style="left:773px;width:369px;top:348px">Envelope (Back) Option 1</div>
<section class="item envelope-back envelope-back-1">
  <svg viewBox="0 0 369 200" preserveAspectRatio="none">
    <path d="M2 2 L184 30 L367 2" fill="none" stroke="var(--line)" stroke-width="1"/>
  </svg>
</section>
<div class="label" style="left:792px;width:367px;top:449px">Envelope (Back) Option 2</div>
<section class="item envelope-back envelope-back-2">
  <svg viewBox="0 0 367 187" preserveAspectRatio="none">
    <path d="M0 78 L183 187 L367 78" fill="none" stroke="var(--line)" stroke-width="1"/>
    <path d="M0 0 L367 0 L367 38 C290 66 230 96 183 108 C135 96 78 66 0 38Z" fill="var(--red)"/>
    <path d="M0 38 C78 66 135 96 183 108 C230 96 290 66 367 38 L367 43 C290 71 230 101 183 113 C135 101 78 71 0 43Z" fill="var(--gold)"/>
  </svg>
  <div class="brand on-red"><span class="dot"></span>HARBOR PATHWAYS</div>
</section>

</body>
</html>
```